" Somos um sistema que faz a gestão financeira de serviços automotivos como estética automotiva e lava-rápido. A operação acontece no smartphone, tablet ou PDV e a gestão através do site administrativos. São 2 módulos integrados. A cobrança é mensal, semestral e anual. Nosso site é www.velotrix.com.br "

```html
<!DOCTYPE html>
<html lang="pt-BR">
<head>
<meta charset="utf-8">
<title>Velotrix – Flyer</title>
<link rel="stylesheet" href="https://fonts.googleapis.com/css2?family=Poppins:wght@400;500;600;700&display=swap">
<style>
  :root{
    --bg:#d9dadc;
    --navy:#253f78;
    --navy-deep:#1c3163;
    --green:#35c46a;
    --white:#ffffff;
    --soft:#c9d4ee;
  }
  *{box-sizing:border-box;margin:0;padding:0}
  html,body{width:1200px;height:1200px;overflow:hidden}
  body{background:var(--bg);font-family:"Poppins",sans-serif;color:var(--white);position:relative}
  .flyer{position:absolute;top:100px;width:480px;height:1000px;background:var(--navy);overflow:hidden;box-shadow:0 8px 24px rgba(0,0,0,.18)}
  .flyer--front{left:90px}
  .flyer--back{left:630px}
  .brand{position:absolute;top:52px;left:44px;display:flex;align-items:center;gap:14px}
  .brand-mark{width:40px;height:40px;background:var(--green);border-radius:6px}
  .brand-name{font-size:34px;font-weight:700;letter-spacing:-.5px}
  .photo{position:absolute;top:150px;left:0;width:480px;height:520px;
    background:radial-gradient(ellipse at 55% 45%,#6f86b3 0%,#4b6499 40%,#2f4b86 70%,var(--navy) 100%)}
  .front-copy{position:absolute;left:44px;right:44px;bottom:60px}
  .front-title{font-size:30px;line-height:1.25;font-weight:400}
  .front-title strong{color:var(--green);font-weight:700}
  .front-sub{margin-top:28px;font-size:19px;line-height:1.4;color:var(--soft)}
  .back-title{position:absolute;top:125px;left:44px;right:44px;font-size:30px;line-height:1.15;font-weight:700;text-transform:uppercase}
  .benefits{position:absolute;top:220px;left:44px;list-style:none;border-left:2px solid var(--white);padding-left:22px}
  .benefits li{position:relative;font-size:15px;line-height:1.2;margin-bottom:10px;color:var(--soft)}
  .benefits li::before{content:"";position:absolute;left:-29px;top:5px;width:12px;height:12px;border-radius:50%;background:var(--white)}
  .tab{position:absolute;width:30px;height:50px;background:var(--green);border-radius:14px}
  .tab--right{right:-15px;top:340px}
  .tab--left{left:-15px;top:480px}
  .trial-title{position:absolute;top:445px;left:44px;right:30px;font-size:30px;line-height:1.15;font-weight:400}
  .trial-title strong{display:block;font-weight:700}
  .perks{position:absolute;top:555px;left:44px;list-style:none}
  .perks li{font-size:20px;line-height:1.4}
  .perks li::before{content:"• "}
  .contacts{position:absolute;top:815px;left:44px;list-style:none}
  .contacts li{display:flex;align-items:center;gap:14px;font-size:19px;margin-bottom:16px}
  .contacts svg{width:24px;height:24px;flex:none}
</style>
</head>
<body>
  <section class="flyer flyer--front">
    <div class="brand"><span class="brand-mark"></span><span class="brand-name">Velotrix</span></div>
    <div class="photo" role="img" aria-label="Foto de um profissional sorrindo encostado em um carro em um lava-rápido"></div>
    <div class="front-copy">
      <p class="front-title">Sistema de gestão para <strong>estética automotiva</strong> ou <strong>lava-rápido</strong></p>
      <p class="front-sub">Mais tempo para seu negócio crescer e seu cliente agradecer. Facilitou?</p>
    </div>
  </section>

  <section class="flyer flyer--back">
    <div class="brand"><span class="brand-mark"></span><span class="brand-name">Velotrix</span></div>
    <h2 class="back-title">Faça nosso teste<br>e sinta os benefícios!</h2>
    <ul class="benefits">
      <li>Aumento de produtividade</li>
      <li>Maior fidelização do cliente</li>
      <li>Maior percepção de qualidade pelo cliente</li>
      <li>Menos tempo gasto na gestão</li>
      <li>Mais tempo para crescer</li>
    </ul>
    <span class="tab tab--right"></span>
    <span class="tab tab--left"></span>
    <h3 class="trial-title">Faça nosso teste de <strong>30 dias de teste grátis</strong></h3>
    <ul class="perks">
      <li>Sem compromisso</li>
      <li>Sem cadastro de cartão</li>
      <li>Sem investimento inicial</li>
      <li>Com treinamento</li>
      <li>Com acesso completo</li>
      <li>Com suporte</li>
    </ul>
    <ul class="contacts">
      <li><svg viewBox="0 0 24 24" fill="none" stroke="#fff" stroke-width="2"><path d="M5 3h4l2 5-3 2a11 11 0 0 0 6 6l2-3 5 2v4a2 2 0 0 1-2 2A17 17 0 0 1 3 5a2 2 0 0 1 2-2z"/></svg>21 9000 12 345</li>
      <li><svg viewBox="0 0 24 24"><circle cx="12" cy="12" r="9" fill="none" stroke="#fff" stroke-width="2"/></svg>sistema.velotrix</li>
      <li><svg viewBox="0 0 24 24" fill="none" stroke="#fff" stroke-width="2" stroke-linejoin="round"><path d="M5 3l14 8-6 2-2 6z"/></svg>www.velotrix.com.br</li>
    </ul>
  </section>
</body>
</html>
```